I need a Cool Physio Postcard / Flyer

HI!
We need a double sided, postcard sized, promotional card (not an actual postcard) to distribute to gyms and sporting clubs, promoting our physiotherapy clinic.
The main colours of our brand are navy blue & white (As seen in sample files).
I want it to be HORIZONTAL
On one side i'd like our logo / image.
The name - "Stride & Heel Recovery Collective" and the tagline - "“The nation's trusted lower-leg mending specialists.”
• Fast Rehab for lower limb injury and surgery
• Mobilisation of the foot and ankle
• Hands on therapy
• National sporting team expertise
• Podiatry (Toe-nail, skin, diabetic foot care, orthotics)
• Video pressure treadmill gait analysis and correction
• Running assessment
• Nordic walking training and sessions
Also our website: www.SHRC-example.com.au & a Facebook icon next to www.Facebook.com/SHRC
Also see the sample image of the runner and blue colouring. I would like this included somewhere on the postcard. I'd like to see some different design options implementing the image in different ways (front or back).
On the other side of the card I want the following text:
"SHRC is Victoria’s leading specialist provider of rehabilitation for Foot & Ankle injury and surgery.
We see our patients through their rehabilitation with an unmatched level of care and expertise.
Whether you’re an elite athlete, a weekend walker or strolling to the office, we provide the highest quality treatment and support to quickly get you back to your usual functional capacity, moving pain free with confidence.
Make an appointment at one of our FOUR Victorian locations today!”
Richmond
Brisk Motion Physio
Level 1, 417 Garnet St
Richmond 3121
1300 492 316 Frankston
Suite 6, 318 Wollaston Drive
Frankston 3199
9432 8155
Brighton
Suite 4, 187 Tern Street
Brighton 3186
9381 4027
Geelong
146 Pellham Terrace
Geelong 3220
5307 6491
Please display our four locations in a similar fashion to the white screenshot ive attached.
The images I included of my draft design are just to provide you an idea or some inspiration of what I’m after. Please feel free to use your creativity.. Good Luck!
Project Deadline Extended
Reason: I accidentally didn't put a design brief in for the first 6 days of the project. The designs only started arriving 4 days ago once I corrected this mistake.
I need more time to provide feedback & get exactly what I want.
Thanks in advance
Reid
Training

```html
<!DOCTYPE html>
<html lang="en">
<head>
<meta charset="utf-8">
<title>SHRC – Locations Card</title>
<link href="https://fonts.googleapis.com/css2?family=Arimo:wght@400;700&display=swap" rel="stylesheet">
<style>
  :root {
    --navy: #2c4a78;
    --navy-panel: rgba(38, 72, 124, 0.9);
    --band: rgba(88, 112, 155, 0.85);
    --ink: #111111;
    --ink-soft: #1a1a1a;
    --panel-ink: #ffffff;
    --sky-top: #c9c6c2;
    --sky-mid: #ebe8e4;
    --sky-low: #a59e96;
    --white: #ffffff;
  }
  html, body {
    margin: 0;
    padding: 0;
    width: 1200px;
    height: 850px;
    overflow: hidden;
    background: var(--white);
  }
  .card {
    position: relative;
    width: 1200px;
    height: 850px;
    overflow: hidden;
    font-family: "Arimo", Arial, sans-serif;
    color: var(--ink);
  }
  .backdrop {
    position: absolute;
    inset: 0;
    background:
      radial-gradient(ellipse at 55% 40%, rgba(255,255,255,0.7), rgba(255,255,255,0) 60%),
      linear-gradient(180deg, var(--sky-top) 0%, var(--sky-mid) 35%, #d8d3cd 62%, var(--sky-low) 71%, #d6d2cd 82%, #bdb7b0 100%);
  }
  .top-band {
    position: absolute;
    left: 0;
    top: 10px;
    width: 1200px;
    height: 112px;
    background: var(--band);
    border-radius: 10px;
  }
  .brand-box {
    position: absolute;
    left: 851px;
    top: 10px;
    width: 176px;
    height: 114px;
    background: var(--white);
    box-shadow: 2px 2px 4px rgba(0,0,0,0.35);
    display: flex;
    flex-direction: column;
    align-items: center;
    justify-content: center;
    gap: 10px;
    box-sizing: border-box;
    padding: 8px;
  }
  .brand-mark {
    width: 34px;
    height: 34px;
    background: var(--navy);
  }
  .brand-name {
    font-size: 13px;
    font-weight: 700;
    color: var(--navy);
    text-align: center;
    line-height: 1.2;
  }
  .stretch {
    position: absolute;
    margin: 0;
    white-space: nowrap;
    transform-origin: left top;
    text-shadow: 1px 1px 2px rgba(0,0,0,0.25);
  }
  .lead {
    left: 97px;
    top: 160px;
    font-size: 27px;
    font-weight: 700;
    line-height: 34px;
    transform: scaleX(1.2);
  }
  .body-text {
    left: 97px;
    font-size: 31px;
    font-weight: 400;
    color: var(--ink-soft);
    transform: scaleX(1.19);
  }
  .body-text.first { top: 250px; line-height: 37px; }
  .body-text.second { top: 361px; line-height: 38px; }
  .cta {
    left: 95px;
    top: 547px;
    font-size: 26px;
    font-weight: 700;
    line-height: 32px;
    transform: scaleX(1.23);
  }
  .locations {
    position: absolute;
    left: 163px;
    top: 605px;
    width: 870px;
    height: 245px;
    background: var(--navy-panel);
    border-radius: 4px 4px 0 0;
    display: grid;
    grid-template-columns: 425px 1fr;
    grid-template-rows: auto auto;
    row-gap: 20px;
    padding: 14px 0 0 69px;
    box-sizing: border-box;
  }
  .location { color: var(--panel-ink); }
  .location-name {
    margin: 0;
    font-size: 21px;
    font-weight: 700;
    line-height: 24px;
  }
  .location-detail {
    margin: 0;
    font-size: 18px;
    line-height: 21.5px;
    text-transform: uppercase;
  }
</style>
</head>
<body>
<main class="card">
  <div class="backdrop" role="img" aria-label="Photograph of a woman running in silhouette against a hazy sky and distant horizon"></div>

  <div class="top-band"></div>

  <div class="brand-box">
    <span class="brand-mark"></span>
    <span class="brand-name">Stride &amp; Heel Recovery Collective</span>
  </div>

  <p class="stretch lead">SHRC is Victoria’s leading specialist provider of rehabilitation<br>for Foot &amp; Ankle injury and surgery.</p>
  <p class="stretch body-text first">We see our patients through their rehabilitation with an<br>unmatched level of care and expertise.</p>
  <p class="stretch body-text second">Whether you’re an elite athlete, a weekend walker or<br>strolling to the office, we provide the highest quality treatment<br>and support to quickly get you back to your usual functional<br>capacity, moving pain free with confidence.</p>

  <p class="stretch cta">Make an appointment at one of our FOUR Victorian locations today!</p>

  <section class="locations">
    <div class="location">
      <h2 class="location-name">RICHMOND</h2>
      <p class="location-detail">Level 1, 417 Garnet St</p>
      <p class="location-detail">Richmond 3121</p>
      <p class="location-detail">1300 492 316</p>
    </div>
    <div class="location">
      <h2 class="location-name">FRANKSTON</h2>
      <p class="location-detail">Suite 6, 318 Wollaston Drive</p>
      <p class="location-detail">Frankston 3199</p>
      <p class="location-detail">9432 8155</p>
    </div>
    <div class="location">
      <h2 class="location-name">BRIGHTON</h2>
      <p class="location-detail">Suite 4, 187 Tern Street</p>
      <p class="location-detail">Brighton 3186</p>
      <p class="location-detail">9381 4027</p>
    </div>
    <div class="location">
      <h2 class="location-name">GEELONG</h2>
      <p class="location-detail">146 Pellham Terrace</p>
      <p class="location-detail">Geelong 3220</p>
      <p class="location-detail">5307 6491</p>
    </div>
  </section>
</main>
</body>
</html>
```